Vantorski Sound House needs postcard ad for Brevik Keyboard sale!

This postcard should be advertising a limited sales promotion for $5,000.00 minimum trade-in value for your Brevik keyboard when purchasing a new Brevik keyboard. Vantorski Sound House is celebrating its 50th anniversary and is your Brevik Keyboard Dealership.

Target Market(s)

Church

Requirements
Must have
• "$5,000.00" should be prominently featured in this advertisement
Nice to have
• Our company colors are blue and green

```html
<!DOCTYPE html>
<html lang="en">
<head>
<meta charset="utf-8">
<title>Vantorski Sound House – 50th Anniversary Postcard</title>
<link rel="stylesheet" href="https://fonts.googleapis.com/css2?family=Montserrat:ital,wght@0,500;0,700;0,800;0,900;1,800;1,900&display=swap">
<style>
  :root {
    --backdrop: #dcdad7;
    --card: #ffffff;
    --ink: #000000;
    --brand-blue: #1f5fa8;
    --brand-green: #2e9a5b;
    --sky-top: #c9c2bc;
    --sky-glow: #e9dcc2;
    --mountain: #8a898d;
    --lake: #d3c7b5;
    --wood-light: #8a5530;
    --wood-dark: #5a321b;
  }
  * { box-sizing: border-box; margin: 0; padding: 0; }
  html, body {
    width: 1200px; height: 857px; overflow: hidden;
    background: var(--backdrop);
    font-family: "Montserrat", sans-serif;
    color: var(--ink);
  }
  .postcard {
    position: absolute; left: 60px; top: 68px;
    width: 1080px; height: 720px;
    background: var(--card);
    box-shadow: 0 2px 10px rgba(0,0,0,.12);
  }
  .scenic-photo {
    position: absolute; left: 53px; top: 53px;
    width: 616px; height: 612px;
    background: linear-gradient(180deg, var(--sky-top) 0%, var(--sky-glow) 36%, #b7b0aa 46%, var(--mountain) 52%, #a9a4a0 60%, var(--lake) 78%, #e2d8c8 100%);
  }
  .organ-photo {
    position: absolute; left: 310px; top: 370px;
    width: 370px; height: 321px;
    background: linear-gradient(180deg, #b07a4a 0%, var(--wood-light) 30%, var(--wood-dark) 70%, #6e4226 100%);
    border-radius: 3px 3px 6px 6px;
  }
  .details {
    position: absolute; left: 734px; top: 52px; width: 300px;
  }
  .brand {
    display: flex; align-items: center; gap: 10px;
    height: 70px; white-space: nowrap;
    border-top: 2px solid var(--brand-blue); border-bottom: 2px solid var(--brand-blue);
    font-weight: 800; font-size: 21px; letter-spacing: -0.3px;
  }
  .brand-dot { width: 14px; height: 14px; border-radius: 50%; background: var(--brand-green); flex: none; }
  .intro { margin-top: 42px; font-weight: 500; font-size: 18px; }
  .milestone { font-weight: 900; font-size: 112px; line-height: 0.9; letter-spacing: -3px; margin-top: 4px; }
  .milestone-label { font-weight: 700; font-size: 28px; letter-spacing: 6.6px; margin-top: 2px; }
  .event-date {
    margin-top: 22px; padding: 6px 0;
    border-top: 2px solid var(--brand-blue); border-bottom: 2px solid var(--brand-blue);
    font-weight: 800; font-size: 26px; white-space: nowrap;
  }
  .promo { margin-top: 30px; font-weight: 500; font-size: 17px; line-height: 1.25; }
  .promo-amount {
    display: block; font-weight: 900; font-style: italic; font-size: 50px;
    line-height: 1.05; letter-spacing: -1px; margin: 4px 0 6px;
    color: var(--brand-blue);
  }
  .promo strong { font-weight: 800; color: var(--brand-green); }
</style>
</head>
<body>
  <main class="postcard">
    <div class="scenic-photo" role="img" aria-label="Mountain range at sunrise reflected in a calm lake"></div>
    <div class="organ-photo" role="img" aria-label="Three-manual Brevik keyboard console in walnut wood"></div>

    <section class="details">
      <div class="brand"><span class="brand-dot"></span>Vantorski Sound House</div>
      <p class="intro">We are celebrating our</p>
      <p class="milestone">50th</p>
      <p class="milestone-label">Anniversary</p>
      <p class="event-date">December 31st, 2020</p>
      <p class="promo">
        Limited sales promotion
        <span class="promo-amount">$5,000.00</span>
        minimum trade-in value for your organ when purchasing a new <strong>Brevik keyboard</strong>
      </p>
    </section>
  </main>
</body>
</html>
```